Home page graphic design only (NOT WEBSITE DESIGN)

I require a home page to be designed for my new website.
I DO NOT REQUIRE to build a website. We are a rug company specialising in alpaca wool. It is targeted at the high end of the market and hence the graphics of our page requires to reflect this. Our current page is as per attachment and I think it is too basic.
Updates

Target Market(s)

Extremly high net worth individuals where luxury is a requirement

Requirements
Must have
• show of style, luxury, uniqueness. Prefer having bright images.
Nice to have
• a highly sofisticated roomscape where the focus in the rug. See attachment as an example
Should not have
• Not sure

```html
<!DOCTYPE html>
<html lang="en">
<head>
<meta charset="utf-8">
<title>Vellano Fibre – Home</title>
<link href="https://fonts.googleapis.com/css2?family=Lora:wght@400;700&display=swap" rel="stylesheet">
<style>
  :root {
    --backdrop: #676462;
    --page: #231f1f;
    --gold: #c9a54a;
    --text-soft: #b9b5b3;
    --text-strong: #f1eeec;
    --text-nav: #dedad8;
    --text-small: #a8a4a2;
    --wordmark-large: #a39e9c;
    --photo-dark: #3a3636;
    --photo-light: #7a7574;
  }
  * { margin: 0; padding: 0; box-sizing: border-box; }
  html, body { width: 1200px; height: 1200px; overflow: hidden; }
  body { background: var(--backdrop); font-family: "Lora", Georgia, serif; position: relative; }

  .home {
    position: absolute; left: 0; top: 262px;
    width: 960px; height: 540px;
    transform: scale(1.25); transform-origin: top left;
    background: var(--page); overflow: hidden;
  }
  .brand { position: absolute; left: 78px; top: 32px; font-size: 17px; color: var(--gold); }
  .main-nav { position: absolute; right: 47px; top: 32px; display: flex; gap: 18px; font-size: 10.5px; color: var(--text-nav); }

  .hero-title {
    position: absolute; left: 78px; top: 148px; width: 340px;
    font-size: 26px; line-height: 32px; color: var(--text-soft); font-weight: 400;
  }
  .hero-title strong { color: var(--text-strong); font-weight: 700; }

  .cta {
    position: absolute; left: 81px; top: 277px; width: 96px; height: 31px;
    border: 1px solid var(--gold); color: var(--gold); font-size: 8px;
    display: flex; align-items: center; justify-content: center; gap: 10px;
  }
  .regions { position: absolute; left: 80px; top: 340px; display: flex; font-size: 7.5px; color: var(--text-small); }
  .regions span { padding: 0 6px; border-left: 1px solid #555; }
  .regions span:first-child { border-left: none; padding-left: 0; }

  .hero-photo {
    position: absolute; left: 509px; top: 96px; width: 451px; height: 312px;
    background: radial-gradient(ellipse at 70% 20%, var(--photo-light), transparent 60%),
                linear-gradient(135deg, var(--photo-light) 0%, var(--photo-dark) 55%, #2b2828 100%);
  }
  .wordmark-large {
    position: absolute; left: 406px; top: 362px;
    font-size: 64px; line-height: 1; color: var(--wordmark-large); white-space: nowrap;
  }

  .social { position: absolute; left: 78px; top: 506px; display: flex; gap: 6px; }
  .social span { width: 15px; height: 15px; border-radius: 50%; background: var(--text-small); display: block; }
  .copyright { position: absolute; right: 50px; top: 510px; font-size: 7.5px; color: var(--text-small); }
</style>
</head>
<body>
  <main class="home">
    <div class="brand">Vellano Fibre</div>
    <nav class="main-nav">
      <span>Home</span><span>Collections</span><span>Our story</span><span>About us</span>
      <span>FAQ</span><span>Publications</span><span>News &amp; Events</span><span>Contact us</span>
    </nav>

    <h1 class="hero-title">Exquisite luxury carpenting and area rugs made from pure <strong>Peruvian alpaca</strong></h1>

    <div class="cta">See collections
      <svg width="6" height="9" viewBox="0 0 6 9"><path d="M1 1l3.5 3.5L1 8" fill="none" stroke="currentColor" stroke-width="1.1"/></svg>
    </div>

    <div class="regions">
      <span>Australia</span><span>USA</span><span>Europe</span><span>UK</span><span>Asia</span><span>UAE</span>
    </div>

    <div class="hero-photo" role="img" aria-label="Close-up photograph of long grey alpaca rug pile"></div>
    <div class="wordmark-large">Vellano Fibre</div>

    <div class="social" aria-label="Social media links">
      <span></span><span></span><span></span><span></span><span></span>
    </div>
    <div class="copyright">Copyright @2020 Vellano Fibre - Australia - Head Office - Suite 8 / Unit 112 -140 Harbour Mill Road</div>
  </main>
</body>
</html>
```